New Company Business Card Design

I have a new company logo and I want a new business card design. I dont know if the logo file i attached is in the correct format or quality. We are a New York City Specialty construction Firm specializing in high risk out of the box projects. I want a simple and classy business card that people will his card is as crisp as the work his company does.

Target Market(s)

Clients in the heavy construction industry in New York City

Industry/Entity Type

Construction Company

Contact Information for Business Card

Simple Classy - DIFFERENT

Font styles to use
Other font styles liked:
• Mach the logo font in some way

Colors

Designer to choose colors to be used in the design.

Requirements
Must have
• Uniqueness
Nice to have
• Nothing particular - Just different and classy - Timeless
Should not have
• Goofy Shit or Gimmicky shit

```html
<!DOCTYPE html>
<html lang="en">
<head>
<meta charset="utf-8">
<title>Kedron Builders – Business Card</title>
<link rel="stylesheet" href="https://fonts.googleapis.com/css2?family=Archivo:wght@700;800;900&display=swap">
<style>
  :root {
    --page: #e4e4e2;
    --card: #f7f7f6;
    --map-light: #f1f1f0;
    --map-mid: #e2e2e1;
    --brand-blue: #1a7ec4;
    --ink: #161616;
    --band: #141414;
    --band-text: #ffffff;
    --icon-blue: #1f86c9;
  }
  * { box-sizing: border-box; margin: 0; padding: 0; }
  html, body { width: 1200px; height: 900px; overflow: hidden; }
  body {
    background: var(--page);
    font-family: "Archivo", Arial, sans-serif;
    position: relative;
  }
  .card {
    position: absolute;
    left: 290px;
    width: 620px;
    height: 354px;
    background: var(--card);
    overflow: hidden;
    box-shadow: 0 6px 18px rgba(0,0,0,0.18);
  }
  .card--front { top: 70px; }
  .card--back { top: 476px; }
  .street-map {
    position: absolute;
    inset: 0;
    background: radial-gradient(ellipse at 35% 55%, var(--map-mid) 0%, var(--map-light) 55%, var(--card) 100%);
  }
  .wordmark {
    position: absolute;
    color: var(--brand-blue);
    font-weight: 900;
    letter-spacing: 0.02em;
    display: flex;
    align-items: center;
    gap: 12px;
    white-space: nowrap;
  }
  .wordmark__square {
    width: 0.8em;
    height: 0.8em;
    background: var(--brand-blue);
  }
  .card--front .wordmark {
    font-size: 40px;
    left: 50%;
    top: 50%;
    transform: translate(-50%, -50%);
  }
  .card--back .wordmark {
    font-size: 24px;
    right: 34px;
    top: 52px;
  }
  .contact-web {
    position: absolute;
    right: 40px;
    top: 176px;
    text-align: right;
    font-weight: 800;
    font-size: 14px;
    line-height: 1.25;
    color: var(--ink);
    letter-spacing: 0.03em;
  }
  .person {
    position: absolute;
    left: 36px;
    top: 186px;
  }
  .person__name {
    color: var(--brand-blue);
    font-weight: 800;
    font-size: 22px;
    letter-spacing: 0.01em;
  }
  .person__title {
    font-weight: 800;
    font-size: 13px;
    letter-spacing: 0.04em;
    color: var(--ink);
    margin-top: 3px;
  }
  .phones {
    list-style: none;
    margin-top: 10px;
  }
  .phones li {
    display: flex;
    align-items: center;
    gap: 8px;
    font-weight: 800;
    font-size: 15px;
    color: var(--ink);
    letter-spacing: 0.03em;
    line-height: 1.5;
  }
  .phones .spacer { width: 16px; }
  .phones svg { width: 16px; height: 16px; }
  .address-band {
    position: absolute;
    left: 30px;
    right: 30px;
    bottom: 28px;
    height: 34px;
    background: var(--band);
    color: var(--band-text);
    font-weight: 800;
    font-size: 15px;
    letter-spacing: 0.03em;
    display: flex;
    align-items: center;
    padding-left: 16px;
  }
</style>
</head>
<body>
  <section class="card card--front" aria-label="Business card front">
    <div class="street-map" role="img" aria-label="Faint street map of the city as card background"></div>
    <div class="wordmark"><span class="wordmark__square"></span>KEDRON BUILDERS, INC.</div>
  </section>

  <section class="card card--back" aria-label="Business card back">
    <div class="street-map" role="img" aria-label="Faint street map of the city as card background"></div>
    <div class="wordmark"><span class="wordmark__square"></span>KEDRON BUILDERS, INC.</div>

    <div class="contact-web">
      <p>MARCUS@KEDRON.COM</p>
      <p>KEDRON.COM</p>
    </div>

    <div class="person">
      <h1 class="person__name">Marcus T. Albrecht</h1>
      <p class="person__title">MANAGING DIRECTOR</p>
      <ul class="phones">
        <li><span class="spacer"></span>555 014 2231</li>
        <li>
          <svg viewBox="0 0 16 16" aria-hidden="true">
            <rect width="16" height="16" rx="3" fill="var(--icon-blue)"/>
            <rect x="5" y="2.5" width="6" height="11" rx="1.2" fill="none" stroke="#fff" stroke-width="1.4"/>
            <circle cx="8" cy="11.3" r="0.8" fill="#fff"/>
          </svg>
          555 018 7740
        </li>
      </ul>
    </div>

    <div class="address-band">118 Harbor Yard Road - Linden, New Jersey 07036</div>
  </section>
</body>
</html>
```